Rex Tollbridge (Burn The Stack) CD Cover Design

Professional Cd cover design needed. No photo of the artist necessary for this cover. You can search Rex Tollbridge on YouTube for a feel of the artist, inspiration, etc. Song (Burn The Stack)!

Target Market(s)

Big money makers , Hustlers, those who don't mind spending cash.

Colors

Designer to choose colors to be used in the design.

Requirements
Nice to have
• Any symbols related to money.

```html
<!DOCTYPE html>
<html lang="en">
<head>
<meta charset="utf-8">
<title>Rex Tollbridge – Burn The Stack</title>
<link rel="stylesheet" href="https://fonts.googleapis.com/css2?family=UnifrakturMaguntia&family=Alegreya+Sans+SC:wght@400&family=Righteous&display=swap">
<style>
  :root {
    --bg-deep: #0b0b0b;
    --bg-mid: #1a1a1a;
    --label: #77776c;
    --value: #cfcfc8;
    --title: #8a8a7e;
    --artist: #d8d8d8;
    --spark: #ffffff;
  }
  html, body {
    margin: 0;
    padding: 0;
    width: 1200px;
    height: 1200px;
    overflow: hidden;
    background: var(--bg-deep);
  }
  .cover {
    position: relative;
    width: 1200px;
    height: 1200px;
    background: radial-gradient(ellipse at 50% 40%, var(--bg-mid) 0%, #121212 55%, var(--bg-deep) 100%);
    font-family: "Alegreya Sans SC", sans-serif;
  }
  .quilt-texture {
    position: absolute;
    inset: 0;
  }
  .line {
    position: absolute;
    left: 0;
    width: 1200px;
    text-align: center;
    white-space: nowrap;
    color: var(--label);
    font-size: 30px;
    letter-spacing: 0.5px;
  }
  .line .value { color: var(--value); }
  .song-title {
    top: 292px;
    font-family: "UnifrakturMaguntia", serif;
    font-size: 82px;
    color: var(--title);
    letter-spacing: 2px;
  }
  .spark {
    display: inline-block;
    width: 14px;
    height: 14px;
    border-radius: 50%;
    background: radial-gradient(circle, var(--spark) 0%, #bbb 45%, rgba(255,255,255,0) 75%);
    vertical-align: middle;
    margin: 0 28px;
    position: relative;
    top: -10px;
  }
  .written { top: 440px; }
  .artist-name {
    font-family: "Righteous", sans-serif;
    color: var(--artist);
    font-size: 31px;
    letter-spacing: 1px;
    margin-left: 8px;
  }
  .produced { top: 536px; }
  .artwork  { top: 628px; }
  .rights   { top: 720px; }
  .notice   { top: 768px; }
  .exec     { top: 862px; }
  .label-mark {
    position: absolute;
    left: 40px;
    top: 1100px;
    display: flex;
    align-items: center;
    gap: 10px;
    color: var(--label);
    font-size: 26px;
  }
  .label-mark .square {
    width: 18px;
    height: 18px;
    background: var(--label);
  }
</style>
</head>
<body>
  <main class="cover">
    <svg class="quilt-texture" role="img" aria-label="Dark quilted leather texture background" width="1200" height="1200">
      <rect width="1200" height="1200" fill="rgba(40,40,40,0.15)"/>
    </svg>

    <h1 class="line song-title"><span class="spark"></span>Burn The Stack<span class="spark"></span></h1>

    <p class="line written">Written by: <span class="artist-name">REX TOLLBRIDGE</span></p>
    <p class="line produced">Produced by: <span class="value">Beatsmith K for Fury Records, Inc.</span></p>
    <p class="line artwork">Artwork Provided by: <span class="value">Northlight Studio</span></p>
    <p class="line rights">© 2018 ALL RIGHTS RESERVED</p>
    <p class="line notice">Unauthorized Duplication Is A Violation Of Applicable Laws</p>
    <p class="line exec">Executive Producer: <span class="value">Fury</span></p>

    <div class="label-mark"><span class="square"></span><span>Fury Records</span></div>
  </main>
</body>
</html>
```